Interior Design business card design

I am an interior decorator - dont want to specify decorating more just design.
Want organic looking logo - charcoal and white - with touch of lime green.
Like the idea of some sort of spiral in corner but writing in a line
want lower case, carlamintowe as one and designs in different font underneath. Maybe using c and m as logo.
More modern than traditional. My clients are mid to top end residential

Target Market(s)

medium to top end homeowners

Industry/Entity Type

Residential

Contact Information for Business Card

Carla Mintowe Designs
58 Fallowmere ave
Tindarra 2188 NSW
Tel 0417869214
carlamintowe@quellnet.com.au

Logo Text

Carla Mintowe Designs

Logo styles of interest
Abstract Logo
Lettermark Logo
Requirements
Must have
• Name address ph and e mail
Nice to have
• Contemporary
smart but organic
Should not have
• no traditional fonts

```html
<!DOCTYPE html>
<html lang="en">
<head>
<meta charset="utf-8">
<title>Carla Mintowe Designs – Business Card</title>
<link href="https://fonts.googleapis.com/css2?family=Roboto:wght@300&display=swap" rel="stylesheet">
<style>
  :root {
    --backdrop: #3b2619;
    --card-lime: #abc12b;
    --ink-charcoal: #2a2a22;
    --ink-muted: #6f7a2a;
  }
  html, body {
    margin: 0;
    padding: 0;
    width: 1200px;
    height: 721px;
    overflow: hidden;
    background: var(--backdrop);
  }
  .canvas {
    position: relative;
    width: 1200px;
    height: 721px;
  }
  .business-card {
    position: absolute;
    left: 90px;
    top: 77px;
    width: 1020px;
    height: 566px;
    display: block;
  }
  .card-face { fill: var(--card-lime); }
  .line-art {
    fill: none;
    stroke: var(--ink-charcoal);
    stroke-width: 0.8;
    stroke-linecap: round;
  }
  .name-line {
    font-family: "Roboto", Arial, sans-serif;
    font-weight: 300;
    font-size: 24px;
    letter-spacing: 0.6px;
    fill: var(--ink-charcoal);
  }
  .contact-details {
    font-family: "Roboto", Arial, sans-serif;
    font-weight: 300;
    font-size: 9px;
    fill: var(--ink-muted);
  }
</style>
</head>
<body>
<main class="canvas">
  <svg class="business-card" viewBox="0 0 460 255" xmlns="http://www.w3.org/2000/svg" aria-label="Carla Mintowe Designs business card">
    <defs>
      <clipPath id="card-edge">
        <rect x="0" y="0" width="460" height="255"/>
      </clipPath>
    </defs>
    <rect class="card-face" x="0" y="0" width="460" height="255"/>
    <g clip-path="url(#card-edge)">
      <circle class="line-art corner-mark" cx="84" cy="40" r="74"/>
      <path class="line-art wave-line" d="M0 180 C 30 190, 65 192, 100 186 C 150 177, 200 152, 260 133 C 320 114, 400 100, 460 104"/>
    </g>
    <text class="name-line" x="182" y="140" transform="rotate(-13 182 140)">carla mintowe</text>
    <text class="contact-details">
      <tspan x="192" y="199">Carla Mintowe Designs 58 Fallowmere ave</tspan>
      <tspan x="192" y="211">Tindarra 2188 NSW&#160;&#160;&#160;Tel 0417869214</tspan>
      <tspan x="192" y="224">carlamintowe@quellnet.com.au</tspan>
    </text>
  </svg>
</main>
</body>
</html>
```